Counsel Atelier

we need all the matirials for the office to speak with the internet site
www.cunatel.example

look stilish and modern yet very respecteble

our logo needs to be our logo and some times

just the letters " Cunatel " done nicely.

We need to send e mails with a design

Firm paper

and our gmail products to look nice when we use google docs

so we need a place for

lawers names and

the cunatel

and logo

and address

and some one to help us do it all

Target Market(s)

Big firms

Industry/Entity Type

Law Firm

Font styles to use
Serif

Requirements
Must have
• Rememrable
• Different yet respectable
• For multi languages
• LAW
• B
• LAWYERS
• BOUTIQUE
Nice to have
• Clean Design
• impressive
• i put on a new card i liked
• We should not put any decorations and beautiful logo
• it's against the law for lawyers
• I have a card that proves that we are smart and boutiques
• This card that I attached as an example
• Makes you little work, and certainly - apart from everyone
• Would love this design idea
• The numbers stated hiding it from top to bottom
• I put my real information integration profile
• The thing is that people should enlighten other options and other card
• This should be accessible designer fee changes
• Still very respectable and serious
• it needs to say among other creative stuff
• Counsel atelier CUNATEL
• TOMAS VELLINGRO
• 052-7164291
• 1@cunatel.example
• www.cunatel.example
• but any smart idea
Should not have
• We have a problam
• It turns out that the law of the Bar Association in
• Our country
• Do not allow to put the firm logo on business cards
• Or office paper
• the logo can only be letters and names
• So we should convey the idea of all sorts of areas along
• As we tried with our logo
• Through the letters themselves
• And their integration with each other

```html
<!DOCTYPE html>
<html lang="en">
<head>
<meta charset="utf-8">
<title>Counsel Atelier — Stationery</title>
<link rel="stylesheet" href="https://fonts.googleapis.com/css2?family=Arimo:wght@400;700&family=Questrial&family=Pinyon+Script&display=swap">
<style>
:root{
  --backdrop:#d2d2d4;
  --ink:#1d1d1d;
  --charcoal:#2e2e2f;
  --charcoal-deep:#262627;
  --paper:#f7f7f7;
  --ghost-light:#ececec;
  --ghost-dark:#383839;
  --muted:#6f6f6f;
  --silver:#bfbfbf;
  --rule:#8a8a8a;
}
*{margin:0;padding:0;box-sizing:border-box}
html,body{width:1200px;height:1068px;overflow:hidden;background:var(--backdrop)}
.sheet-set{position:relative;width:1200px;height:1068px;font-family:"Questrial",sans-serif;color:var(--ink)}
.piece{position:absolute;overflow:hidden}
.wordmark{font-family:"Arimo",sans-serif;font-weight:700;letter-spacing:-0.5px;color:var(--ink);line-height:1}
.ghost{position:absolute;font-family:"Arimo",sans-serif;font-weight:700;letter-spacing:-2px;line-height:1;white-space:nowrap}
.vertical{writing-mode:vertical-rl;transform:rotate(180deg)}
.contact{font-size:4.6px;line-height:1.45;color:var(--muted);white-space:nowrap}
.contact b{color:var(--ink)}

/* presentation folder */
.folder-panel{top:102px;width:323px;height:436px;background:var(--charcoal);border-radius:3px}
.folder-back{left:94px}
.folder-front{left:420px}
.folder-front .ghost{right:6px;top:26px;font-size:112px;color:var(--ghost-dark)}
.folder-back .contact{position:absolute;left:25px;bottom:20px;color:#9a9a9a}
.folder-back .contact b{color:#d0d0d0}
.folder-front .wordmark{position:absolute;left:214px;top:368px;font-size:27px;color:var(--silver)}
.folder-front .site{position:absolute;left:215px;top:395px;font-size:5px;color:#9a9a9a}
.folder-front .site b{color:#d0d0d0}

/* envelope */
.envelope{left:792px;top:110px;width:315px;height:164px;background:var(--paper)}
.envelope-flap{position:absolute;left:0;top:0;width:100%;height:50px;background:var(--charcoal-deep)}
.envelope-flap .wordmark{position:absolute;left:50%;top:20px;font-size:10px;color:var(--silver);transform:translateX(-50%) rotate(180deg)}
.envelope .wordmark.lead{position:absolute;left:16px;top:60px;font-size:16px}
.envelope .contact{position:absolute;left:83px;top:62px}
.envelope .ghost{left:16px;top:110px;font-size:58px;color:var(--ghost-light)}

/* compliments slip */
.slip{left:792px;top:301px;width:299px;height:140px;background:var(--paper)}
.slip .wordmark{position:absolute;left:20px;top:20px;font-size:16px}
.slip .ghost{right:14px;top:-8px;font-size:46px;color:var(--ghost-light)}
.slip .contact{position:absolute;left:20px;top:112px}
.slip .greeting{position:absolute;right:14px;top:113px;font-family:"Pinyon Script",cursive;font-size:12px;color:#333}

/* business cards */
.card{top:478px;width:122px;height:68px;background:var(--charcoal)}
.card-front{left:792px}
.card-back{left:945px}
.card-front .wordmark{position:absolute;left:8px;top:12px;font-size:8px;color:var(--silver)}
.card-front .ghost{left:36px;top:-4px;font-size:24px;color:var(--ghost-dark)}
.card-front .holder{position:absolute;left:8px;top:47px;font-size:4.6px;line-height:1.3;color:var(--silver);text-align:center}
.card-front .contact{position:absolute;left:44px;top:47px;font-size:3.3px;color:#9a9a9a}
.card-back .pattern{position:absolute;inset:0;background:linear-gradient(160deg,#2b2b2c,#333334)}

/* letterhead */
.letter{top:581px;width:300px;height:423px;background:var(--paper)}
.letterhead{left:94px}
.continuation{left:443px}
.fax{left:791px}
.letterhead .wordmark,.fax .wordmark{position:absolute;left:19px;top:21px;font-size:17px}
.letter .contact.right{position:absolute;right:22px;top:21px;text-align:right}
.letterhead .ghost{left:1px;bottom:-4px;font-size:88px;color:var(--ghost-light)}
.continuation .wordmark{position:absolute;right:15px;top:14px;font-size:11px}

/* fax sheet */
.fax .contact.right{right:96px}
.fax-title{position:absolute;right:20px;top:16px;font-family:"Arimo",sans-serif;font-size:29px;color:var(--ink);letter-spacing:0.5px}
.fax-grid{position:absolute;left:19px;top:69px;width:259px;border-collapse:collapse;font-family:"Arimo",sans-serif;font-size:4.4px;font-weight:700}
.fax-grid td{border:0.6px solid var(--rule);height:9.2px;padding:0 3px}
.fax-grid td.label{width:27px}
.fax-flags{position:absolute;left:19px;top:126px;width:259px;display:flex;border:0.6px solid var(--rule);background:#eeeeee}
.fax-flags span{flex:1;font-family:"Arimo",sans-serif;font-weight:700;font-size:4.2px;text-align:center;padding:1.8px 0;border-right:0.6px solid var(--rule)}
.fax-flags span:last-child{border-right:0}
.fax-flags i{display:inline-block;width:3px;height:3px;border:0.5px solid #555;margin-right:2px;vertical-align:-0.4px}
.fax-comments{position:absolute;left:19px;top:134px;width:259px;height:255px;border:0.6px solid var(--rule);border-top:0}
.fax-comments p{font-family:"Arimo",sans-serif;font-size:4.4px;text-align:center;margin-top:7px}
</style>
</head>
<body>
<main class="sheet-set">

  <section class="piece folder-panel folder-back">
    <p class="contact">2190 Harlow Avenue NW, Suite 310, Weston<br><b>T:</b> 052-7164291 · <b>E:</b> 1@cunatel.example<br><b>www.cunatel.example</b></p>
  </section>
  <section class="piece folder-panel folder-front">
    <span class="ghost vertical">cunatel</span>
    <span class="wordmark">cunatel</span>
    <p class="site">www.<b>cunatel</b>.example</p>
  </section>

  <section class="piece envelope">
    <div class="envelope-flap"><span class="wordmark">cunatel</span></div>
    <span class="wordmark lead">cunatel</span>
    <p class="contact">2190 Harlow Avenue NW<br>Suite 310, Weston</p>
    <span class="ghost">cunatel</span>
  </section>

  <section class="piece slip">
    <span class="ghost">cunatel</span>
    <span class="wordmark">cunatel</span>
    <p class="contact">2190 Harlow Avenue NW, Suite 310, Weston<br><b>T:</b> 052-7164291 · <b>E:</b> 1@cunatel.example<br>www.<b>cunatel</b>.example</p>
    <p class="greeting">With Compliments</p>
  </section>

  <section class="piece card card-front">
    <span class="ghost">cunatel</span>
    <span class="wordmark">cunatel</span>
    <p class="holder">TOMAS<br>VELLINGRO</p>
    <p class="contact">2190 Harlow Avenue NW, Suite 310, Weston<br>T: 052-7164291 · E: 1@cunatel.example<br>www.cunatel.example</p>
  </section>
  <section class="piece card card-back">
    <div class="pattern" role="img" aria-label="Card back with a dark tone-on-tone repeat of the firm name"></div>
  </section>

  <section class="piece letter letterhead">
    <span class="wordmark">cunatel</span>
    <p class="contact right">2190 Harlow Avenue NW, Suite 310, Weston<br><b>T:</b> 052-7164291 · <b>E:</b> 1@cunatel.example<br>www.<b>cunatel</b>.example</p>
    <span class="ghost vertical">cunatel</span>
  </section>

  <section class="piece letter continuation">
    <span class="wordmark">cunatel</span>
  </section>

  <section class="piece letter fax">
    <span class="wordmark">cunatel</span>
    <p class="contact right">2190 Harlow Avenue NW, Suite 310, Weston<br><b>T:</b> 052-7164291 · <b>E:</b> 1@cunatel.example<br>www.<b>cunatel</b>.example</p>
    <h1 class="fax-title">FAX</h1>
    <table class="fax-grid">
      <tr><td class="label">To:</td><td></td><td class="label">From:</td><td></td></tr>
      <tr><td class="label">Fax:</td><td></td><td class="label">Pages:</td><td></td></tr>
      <tr><td class="label">Phone:</td><td></td><td class="label">Date:</td><td></td></tr>
      <tr><td class="label">Re:</td><td></td><td class="label">CC:</td><td></td></tr>
    </table>
    <div class="fax-flags">
      <span><i></i>Urgent</span>
      <span><i></i>For Review</span>
      <span><i></i>Please Comment</span>
      <span><i></i>Please Reply</span>
      <span><i></i>Please Recycle</span>
    </div>
    <div class="fax-comments"><p>COMMENTS:</p></div>
  </section>

</main>
</body>
</html>
```